Stationary package for VORELO
VORELO is an outdoor and camping supplies distribution company
Professional
Yousef K Haddadin
Director
#17 Sahra Trade Gardens
Dubai
UAE
pinetrail@mailbox-ex.test
www.vorelo-supply.test

```html
<!DOCTYPE html>
<html lang="en">
<head>
<meta charset="utf-8">
<title>Vorelo Business Card</title>
<link href="https://fonts.googleapis.com/css2?family=Open+Sans:ital,wght@0,400;0,600;0,800;1,400;1,700&display=swap" rel="stylesheet">
<style>
  :root {
    --backdrop: #e9e6e2;
    --card: #ffffff;
    --ink: #3a3a3c;
    --muted: #6b6b6d;
    --brown: #6b4218;
    --grey: #58585a;
    --grey-light: #9a9a9c;
  }
  html, body {
    margin: 0;
    width: 1200px;
    height: 914px;
    overflow: hidden;
    background: var(--backdrop);
    font-family: "Open Sans", sans-serif;
  }
  .business-card {
    position: absolute;
    left: 75px;
    top: 157px;
    width: 1050px;
    height: 600px;
    background: var(--card);
    box-shadow: 0 10px 30px rgba(0,0,0,.18);
    overflow: hidden;
  }
  .card-swoosh {
    position: absolute;
    inset: 0;
  }
  .brand {
    position: absolute;
    left: 80px;
    top: 120px;
    display: flex;
    align-items: center;
    gap: 16px;
  }
  .brand-mark {
    width: 22px;
    height: 22px;
    background: var(--ink);
  }
  .brand-name {
    font-weight: 800;
    font-size: 76px;
    letter-spacing: 1px;
    color: var(--ink);
    line-height: 1;
  }
  .contact-list {
    position: absolute;
    left: 80px;
    top: 248px;
    margin: 0;
    padding: 0;
    list-style: none;
    font-size: 17px;
    color: var(--muted);
    line-height: 27px;
  }
  .contact-list li {
    display: flex;
    align-items: center;
    gap: 10px;
  }
  .contact-list li.continued { padding-left: 28px; }
  .contact-icon {
    width: 18px;
    height: 18px;
    flex: none;
  }
  .signatory {
    position: absolute;
    right: 62px;
    bottom: 62px;
    text-align: right;
  }
  .signatory-name {
    font-weight: 700;
    font-style: italic;
    font-size: 21px;
    color: var(--brown);
  }
  .signatory-role {
    font-style: italic;
    font-size: 17px;
    color: var(--muted);
  }
</style>
</head>
<body>
  <div class="business-card">
    <svg class="card-swoosh" width="1050" height="600" viewBox="0 0 1050 600">
      <path d="M700 0 L790 0 C 900 110 990 280 1050 460 L1050 540 C 980 330 880 140 700 0 Z" fill="var(--grey)"/>
      <path d="M790 0 L1050 0 L1050 460 C 990 280 900 110 790 0 Z" fill="var(--brown)"/>
      <path d="M820 0 C 925 100 1000 260 1050 420" fill="none" stroke="var(--grey-light)" stroke-width="4"/>
    </svg>

    <div class="brand">
      <div class="brand-mark"></div>
      <div class="brand-name">VORELO</div>
    </div>

    <ul class="contact-list">
      <li>
        <svg class="contact-icon" viewBox="0 0 18 18"><circle cx="9" cy="9" r="9" fill="var(--brown)"/><path d="M9 4a3 3 0 0 0-3 3c0 2.3 3 6 3 6s3-3.7 3-6a3 3 0 0 0-3-3z" fill="#fff"/></svg>
        #17 Sahra Trade Gardens
      </li>
      <li class="continued">Dubai UAE</li>
      <li>
        <svg class="contact-icon" viewBox="0 0 18 18"><circle cx="9" cy="9" r="9" fill="var(--brown)"/><path d="M6 4.5l2 2-1 1.2c.6 1.3 1.6 2.3 2.9 2.9l1.2-1 2 2-1.2 1.4C8.5 13 5 9.5 4.6 5.7z" fill="#fff"/></svg>
        +971-555-010-123
      </li>
      <li>
        <svg class="contact-icon" viewBox="0 0 18 18"><circle cx="9" cy="9" r="9" fill="var(--brown)"/><rect x="6" y="3.5" width="6" height="11" rx="1.2" fill="#fff"/></svg>
        +971-555-010-456
      </li>
      <li>
        <svg class="contact-icon" viewBox="0 0 18 18"><circle cx="9" cy="9" r="9" fill="var(--brown)"/><rect x="4" y="5.5" width="10" height="7" fill="#fff"/><path d="M4 5.5l5 4 5-4" fill="none" stroke="var(--brown)" stroke-width="1"/></svg>
        pinetrail@mailbox-ex.test
      </li>
      <li>
        <svg class="contact-icon" viewBox="0 0 18 18"><circle cx="9" cy="9" r="9" fill="var(--brown)"/><circle cx="9" cy="9" r="4.5" fill="none" stroke="#fff" stroke-width="1.2"/><path d="M4.5 9h9M9 4.5v9" stroke="#fff" stroke-width="1"/></svg>
        www.vorelo-supply.test
      </li>
    </ul>

    <div class="signatory">
      <div class="signatory-name">Yousef K Haddadin</div>
      <div class="signatory-role">Director</div>
    </div>
  </div>
</body>
</html>
```